Top of the line business card design needed for real estate brokerage

We currently have a business card with our logo but would like to have a revised version. We would love for you to implement your own design that will catch anyone's attention. The theme colors should be black, royal blue, gray/silver, and white.The contact information should be the same as the info on our current business card (picture attached). In the design that we pick, we will need to be able to edit the text so that we can customize the text content for each of our agents. Same goes for the professional picture. There should be an area on the card that each agent can have their professional portrait attached. Please include a version without the picture option as well for agents that do not wish to have a professional picture attached.

```html
<!DOCTYPE html>
<html lang="en">
<head>
<meta charset="utf-8">
<title>Clear Crest Realty – Business Card</title>
<link href="https://fonts.googleapis.com/css2?family=Lato:wght@400;700&display=swap" rel="stylesheet">
<style>
  :root {
    --backdrop: #222222;
    --royal: #0656a8;
    --ink: #1e1e1e;
    --silver: #b9bcc0;
    --paper: #ffffff;
    --mist: #e6e6e6;
  }
  * { margin: 0; padding: 0; box-sizing: border-box; }
  html, body { width: 1189px; height: 1200px; overflow: hidden; }
  body { background: var(--backdrop); font-family: 'Lato', sans-serif; position: relative; }

  .card { position: absolute; left: 171px; width: 856px; height: 489px; overflow: hidden; }
  .card-front { top: 66px; background: var(--paper); }
  .card-back { top: 626px; background: radial-gradient(ellipse at 45% 35%, #ffffff 0%, #f1f1f1 40%, var(--mist) 100%); }

  .skyline {
    position: absolute; left: 66px; top: 12px; width: 730px; height: 286px;
    background: linear-gradient(180deg, rgba(255,255,255,0) 0%, #eceef1 45%, #dfe2e6 100%);
  }
  .brand {
    position: absolute; left: 0; right: 0; top: 316px; height: 64px; text-align: center;
    font-weight: 700; font-size: 50px; line-height: 64px; color: var(--ink); letter-spacing: 0.5px;
    display: flex; justify-content: center; align-items: center; gap: 14px;
  }
  .brand-mark { width: 22px; height: 22px; background: var(--royal); }

  .services-band {
    position: absolute; left: 0; bottom: 0; width: 100%; height: 86px;
    background: var(--royal); color: var(--paper); text-align: center;
    font-size: 22px; line-height: 29px; padding-top: 14px; letter-spacing: 0.2px;
  }

  .agent-name { position: absolute; left: 51px; top: 60px; font-size: 33px; font-weight: 700; color: var(--royal); }
  .agent-title { position: absolute; left: 52px; top: 98px; font-size: 23px; color: var(--ink); }
  .address { position: absolute; left: 51px; top: 170px; font-size: 25px; line-height: 31px; color: var(--ink); }

  .contact-list { position: absolute; left: 51px; top: 276px; list-style: none; }
  .contact-list li { display: flex; align-items: center; height: 34px; font-size: 26px; color: var(--ink); }
  .contact-icon { width: 29px; height: 29px; background: var(--royal); margin-right: 17px; display: flex; align-items: center; justify-content: center; flex-shrink: 0; }

  .web-band {
    position: absolute; left: 0; bottom: 0; width: 510px; height: 51px;
    background: var(--royal); color: var(--paper); font-size: 24px; padding: 10px 0 0 51px;
  }
  .portrait {
    position: absolute; right: 0; top: 55px; width: 350px; height: 434px;
    background: linear-gradient(180deg, #dcdcdc 0%, #c9c2bf 45%, #a7232c 75%, #9c1f28 100%);
  }
</style>
</head>
<body>
  <section class="card card-front">
    <div class="skyline" role="img" aria-label="Line drawing of a city skyline above the brand name"></div>
    <div class="brand"><span class="brand-mark"></span>Clear Crest Realty</div>
    <div class="services-band">
      residential Real Estate | Commercial Estate | Property Management<br>Investments
    </div>
  </section>

  <section class="card card-back">
    <div class="agent-name">Marla Keaton</div>
    <div class="agent-title">Broker</div>
    <div class="address">2400 Harbor Point Dr,Suite 310<br>Coral Bay,FL 33500</div>

    <ul class="contact-list">
      <li><span class="contact-icon">
        <svg width="13" height="21" viewBox="0 0 13 21"><rect x="1" y="1" width="11" height="19" rx="2" fill="none" stroke="#fff" stroke-width="2"/><rect x="3" y="4" width="7" height="6" fill="#fff"/></svg>
      </span>555-214-3086</li>
      <li><span class="contact-icon">
        <svg width="21" height="17" viewBox="0 0 21 17"><path d="M1 6 Q10.5 -1 20 6 L17 8 L14 5 L7 5 L4 8 Z" fill="#fff"/><rect x="4" y="9" width="13" height="7" rx="1" fill="#fff"/></svg>
      </span>555-214-7719</li>
      <li><span class="contact-icon">
        <svg width="21" height="19" viewBox="0 0 21 19"><rect x="5" y="1" width="11" height="6" fill="#fff"/><rect x="1" y="7" width="19" height="8" rx="1" fill="#fff"/><rect x="5" y="12" width="11" height="6" fill="#fff" stroke="#0656a8" stroke-width="1"/></svg>
      </span>555-214-0562</li>
      <li><span class="contact-icon">
        <svg width="21" height="15" viewBox="0 0 21 15"><rect x="1" y="1" width="19" height="13" fill="none" stroke="#fff" stroke-width="2"/><path d="M1 1 L10.5 8 L20 1 M1 14 L8 7 M20 14 L13 7" fill="none" stroke="#fff" stroke-width="1.5"/></svg>
      </span>marla@clearcrestrealty.com</li>
    </ul>

    <div class="web-band">www.clearcrestrealty.com</div>
    <div class="portrait" role="img" aria-label="Agent's professional portrait in a red blazer"></div>
  </section>
</body>
</html>
```